Small pharmacy chain needs a food supplement private label identity, soon to be launched.

We are a Greek pharmacy chain, with 4 Athens locations. We are launching our first food supplements private label, with products sourced from Europe. We now need a fresh, bold-looking, colorful, attractive, modern, product identity for all our future introductions. Our private label logo, namely "TOVANE - Natural Health", has been nationally registered.
In the present phase, we will provide a packaging photo, an English label and our Greek label translation. We expect a completely fresh approach, for a food supplement line to be remembered by our customers. We mostly like modern US vitamin designs.
In a future phase, all additional English product labels will require Greek adaptation.
Label formats will always be "AI" and "PDF".

Target Market(s)

Retail pharmacy customers, health-conscious and in need of food supplementation.

Industry/Entity Type

Pharmacy

Requirements
Must have
• Detailed regulatory texts, as provided in Greek label translation.
• Text and barcode placements as in original label .ai format.
Nice to have
• Common food supplement private label identity.
• Individual products can carry a product-specific photo, e.g. the Cranberry food supplement can carry a cranberry photo.
Should not have
• Any text not in the Greek label translation.

```html
<!DOCTYPE html>
<html lang="el">
<head>
<meta charset="utf-8">
<title>TOVANE – Βιταμίνες & Ιχνοστοιχεία</title>
<link rel="stylesheet" href="https://fonts.googleapis.com/css2?family=Open+Sans:wght@300;400;600&display=swap">
<style>
  :root {
    --page-bg: #ffffff;
    --red-top: #f2412f;
    --red-bottom: #e2261f;
    --red-band: #8f1117;
    --green-top: #9ede33;
    --green-bottom: #84c923;
    --green-band: #2f3b1f;
    --ink-light: #ffffff;
    --ink-soft: rgba(255,255,255,0.85);
  }
  * { margin: 0; padding: 0; box-sizing: border-box; }
  html, body {
    width: 1200px;
    height: 1094px;
    overflow: hidden;
    background: var(--page-bg);
    font-family: "Open Sans", Arial, sans-serif;
  }
  .canvas {
    position: relative;
    width: 1200px;
    height: 1094px;
    display: flex;
    justify-content: center;
    align-items: center;
    gap: 40px;
  }
  .label {
    width: 540px;
    height: 620px;
    display: flex;
    flex-direction: column;
    align-items: center;
    color: var(--ink-light);
    padding-top: 70px;
  }
  .label--red { background: linear-gradient(180deg, var(--red-top), var(--red-bottom)); }
  .label--green { background: linear-gradient(180deg, var(--green-top), var(--green-bottom)); }
  .label--red .pack-band { background: var(--red-band); }
  .label--green .pack-band { background: var(--green-band); }

  .brand-mark {
    width: 52px;
    height: 52px;
    border-radius: 50%;
    border: 3px solid var(--ink-light);
  }
  .brand-name {
    margin-top: 22px;
    font-weight: 400;
    color: var(--ink-light);
    text-align: center;
    line-height: 1;
  }
  .brand-name__main {
    display: block;
    font-size: 64px;
    letter-spacing: 4px;
  }
  .brand-name__sub {
    display: block;
    margin-top: 10px;
    font-size: 16px;
    letter-spacing: 3px;
  }
  .product-title {
    margin-top: 42px;
    text-align: center;
    font-weight: 300;
    line-height: 1;
  }
  .product-title__main {
    display: block;
    font-size: 60px;
  }
  .product-title__sub {
    display: block;
    margin-top: 6px;
    font-size: 26px;
  }
  .product-type {
    margin-top: 20px;
    font-size: 24px;
    font-weight: 400;
  }
  .divider {
    width: 72px;
    height: 4px;
    background: var(--ink-soft);
    margin: 22px 0 18px;
  }
  .benefit {
    font-size: 23px;
    font-weight: 400;
  }
  .pack-band {
    margin-top: 30px;
    width: 430px;
    height: 76px;
    display: flex;
    align-items: center;
    padding: 0 22px;
  }
  .pack-count {
    display: flex;
    flex-direction: column;
    align-items: center;
    line-height: 1;
  }
  .pack-count__num { font-size: 42px; font-weight: 400; }
  .pack-count__unit { font-size: 13px; margin-top: 2px; }
  .pack-sep {
    width: 2px;
    height: 50px;
    background: var(--ink-soft);
    margin: 0 18px;
  }
  .pack-note {
    font-size: 22px;
    line-height: 1.15;
  }
</style>
</head>
<body>
<main class="canvas">

  <section class="label label--red">
    <div class="brand-mark"></div>
    <div class="brand-name">
      <span class="brand-name__main">TOVANE</span>
      <span class="brand-name__sub">NATURAL HEALTH</span>
    </div>
    <h1 class="product-title">
      <span class="product-title__main">ΒΙΤΑΜΙΝΕΣ &amp;</span>
      <span class="product-title__sub">ΙΧΝΟΣΤΟΙΧΕΙΑ</span>
    </h1>
    <p class="product-type">Συμπλήρωμα διατροφής</p>
    <div class="divider"></div>
    <p class="benefit">Ενίσχυση ανοσοποιητικού συστήματος</p>
    <div class="pack-band">
      <div class="pack-count">
        <span class="pack-count__num">30</span>
        <span class="pack-count__unit">Κάψουλες</span>
      </div>
      <div class="pack-sep"></div>
      <p class="pack-note">Κατάλληλο για<br>Χορτοφάγους</p>
    </div>
  </section>

  <section class="label label--green">
    <div class="brand-mark"></div>
    <div class="brand-name">
      <span class="brand-name__main">TOVANE</span>
      <span class="brand-name__sub">NATURAL HEALTH</span>
    </div>
    <h1 class="product-title">
      <span class="product-title__main">ΒΙΤΑΜΙΝΕΣ &amp;</span>
      <span class="product-title__sub">ΙΧΝΟΣΤΟΙΧΕΙΑ</span>
    </h1>
    <p class="product-type">Συμπλήρωμα διατροφής</p>
    <div class="divider"></div>
    <p class="benefit">Ενίσχυση ανοσοποιητικού συστήματος</p>
    <div class="pack-band">
      <div class="pack-count">
        <span class="pack-count__num">30</span>
        <span class="pack-count__unit">Κάψουλες</span>
      </div>
      <div class="pack-sep"></div>
      <p class="pack-note">Κατάλληλο για<br>Χορτοφάγους</p>
    </div>
  </section>

</main>
</body>
</html>
```